Broschüre für Energieberater
Zielgruppe
Unternehmen die zu den KMU´s gehören (kleine und mittlere Unternehmen) haben die Möglichkeit eine Energieberatung über die ZEKV fördern zu lassen. Diese Beratung wird durch unsere Ingenieure durchgeführt und ist für den Kunden völlig kostenneutral. Zum einen erhält er eine 80% Förderung von der ZEKV (Zentralstelle für Kostenausgleich und Versorgung) die restlichen 20% erhält der Kunde von uns als Gutschrift. Wir finanzieren uns somit nur über die Fördergelder des Bundes. Die Vorteile des Kunden sind: Verringerung von Steuern, Einsparung von mindestens 10% an Energie ohne zusätzliche Kosten und somit weniger C0² Ausstoss, was wiederum allen zugute kommt. Somit ein hohes Maß an Umweltbewusstsein! Alle Investitionen die für die Einsparung von Energie von Vorteil sind, werden vom Bund mit bis zu 200.000 Euro gefördert. Voraussetzung eine durchgeführte ZEKV Energieberatung. Somit eine win/win Situation für alle Beteiligten.
Aufgabenstellung
Das Design kann - muss - nicht an unsere Webseite : www.wattlinde-beratung.de angelehnt sein.

```html
<!DOCTYPE html>
<html lang="de">
<head>
<meta charset="utf-8">
<title>Wattlinde – Broschüre Energieberatung</title>
<link rel="stylesheet" href="https://fonts.googleapis.com/css2?family=Kalam:wght@700&family=Arimo:wght@700&display=swap">
<style>
  :root {
    --bg: #a9a9a9;
    --paper: #ececec;
    --blue-light: #8fd0ea;
    --blue-mid: #6bb6dc;
    --blue-dark: #4b96c2;
    --ink: #4d4d4d;
    --cloud-fill: #e4e4e4;
    --claim: #e4f1f7;
    --logo: #737373;
  }
  html, body {
    margin: 0;
    width: 1200px;
    height: 1200px;
    overflow: hidden;
    background: var(--bg);
  }
  .cover {
    position: absolute;
    left: 340px;
    top: 50px;
    width: 520px;
    height: 1100px;
    overflow: hidden;
    background: linear-gradient(160deg, var(--blue-light) 0%, var(--blue-mid) 50%, var(--blue-dark) 100%);
    box-shadow: 0 10px 30px rgba(0,0,0,.25);
  }
  .cover__header {
    position: absolute;
    left: 0; top: 0;
    width: 100%;
    height: 235px;
    background: var(--paper);
  }
  .brand {
    position: absolute;
    left: 40px;
    top: 95px;
    display: flex;
    align-items: center;
    gap: 12px;
    font-family: "Arimo", Arial, sans-serif;
    font-weight: 700;
    font-size: 46px;
    color: var(--logo);
    letter-spacing: -1px;
  }
  .brand__mark {
    width: 22px;
    height: 22px;
    background: var(--blue-mid);
  }
  .thought-art {
    position: absolute;
    left: 40px;
    top: 170px;
    width: 460px;
    height: 420px;
    border-radius: 60px;
    background: var(--cloud-fill);
  }
  .headline {
    position: absolute;
    left: 40px;
    top: 250px;
    width: 460px;
    margin: 0;
    text-align: center;
    font-family: "Kalam", "Comic Sans MS", cursive;
    font-weight: 700;
    font-size: 44px;
    line-height: 60px;
    color: var(--ink);
    transform: rotate(-10deg);
  }
  .claim {
    position: absolute;
    left: 60px;
    top: 860px;
    margin: 0;
    width: 420px;
    font-family: "Arimo", Arial, sans-serif;
    font-weight: 700;
    font-size: 29px;
    line-height: 1.25;
    color: var(--claim);
  }
</style>
</head>
<body>
  <main class="cover">
    <div class="cover__header"></div>
    <div class="brand"><span class="brand__mark"></span>Wattlinde</div>

    <div class="thought-art" role="img" aria-label="Illustration: gezeichnete Gedankenwolke mit drei kleinen Gedankenblasen"></div>
    <h1 class="headline">ENERGIE<br>SPAREN HEIẞT<br>GELD SPAREN!</h1>

    <p class="claim">Erhalten Sie jetzt Ihre staatlich geförderte Energieberatung durch Experten!</p>
  </main>
</body>
</html>
```